We need a website design for an HVAC (Heating & Air Conditioning) Contractor*

Our HVAC client would like to have a more professional looking site as their current one (https://brisvanecomfortworks.example/) is a template site. We will be building the site in-house from the concept.
Items we'd like to incorporate:
- A banner on the homepage that has a click to call plus a form on the right side of the banner
- There is a video on the current website homepage, please find a place to incorporate this.
- We will need to have at least 800 words of content on the homepage, please find space for that (can be a description of a few of the heating / air conditioning services they do). Feel free to use filler content (lorem ipsum) if need be to just show how the content would look

All submissions must have a homepage and a related subpage concept.

Number of Pages Required

1 page

```html
<!DOCTYPE html>
<html lang="en">
<head>
<meta charset="utf-8">
<title>BrisVane Comfort Works — Heating &amp; Air Conditioning</title>
<link href="https://fonts.googleapis.com/css2?family=Montserrat:wght@400;500;600;700;800&family=Raleway:wght@400;500;600&display=swap" rel="stylesheet">
<style>
:root{
  --navy:#1a3263;
  --navy-dark:#15294f;
  --red:#c8261f;
  --grey-band:#e4e4e4;
  --text:#4a4a4a;
  --muted:#6d6d6d;
  --white:#ffffff;
}
*{box-sizing:border-box;margin:0;padding:0}
html,body{width:1200px;height:2846px;overflow:hidden}
body{font-family:"Raleway",sans-serif;color:var(--text);background:var(--white);position:relative}
h1,h2,h3,.nav a,.btn{font-family:"Montserrat",sans-serif}
.wrap{position:absolute;left:0;width:1200px}

/* header */
.site-header{top:0;height:135px}
.brand{position:absolute;left:104px;top:44px;display:flex;align-items:center;gap:10px}
.brand-mark{width:22px;height:22px;background:var(--red)}
.brand-name{font-family:"Montserrat",sans-serif;font-weight:800;font-size:24px;color:var(--navy);line-height:1}
.head-info{position:absolute;top:62px;font-size:13px;line-height:18px}
.head-info b{display:flex;align-items:center;gap:5px;color:var(--red);font-family:"Montserrat",sans-serif;font-weight:600;font-size:13px}
.head-info span{display:block;color:var(--muted);padding-left:15px}
.social{display:flex;gap:3px;margin-top:4px}
.social i{display:block;width:13px;height:13px;background:var(--navy)}

/* nav */
.nav{top:135px;height:41px;background:var(--navy);display:flex;align-items:center}
.nav a{position:absolute;top:0;height:41px;line-height:41px;color:var(--white);font-size:12.5px;font-weight:600;text-decoration:none;text-transform:uppercase}
.nav a.active{background:var(--red);width:92px;text-align:center}

/* hero */
.hero{top:176px;height:537px;background:linear-gradient(100deg,#5d5a55 0%,#7d766d 35%,#a98a63 55%,#8e8f93 75%,#b7bcc2 100%)}
.hero-copy{position:absolute;left:100px;top:97px;color:var(--white)}
.hero-copy h1{font-size:47px;line-height:49px;font-weight:800;text-transform:uppercase}
.hero-copy p{margin-top:20px;margin-left:4px;font-family:"Montserrat",sans-serif;font-size:22.5px;line-height:29px;text-transform:uppercase;font-weight:400}
.hero-actions{position:absolute;left:104px;top:321px;display:flex;gap:18px}
.review-btn{width:173px;height:53px;background:#2f6fd1;display:flex;align-items:center;gap:8px;padding-left:6px;color:var(--white);font-size:11.5px;line-height:13px}
.review-btn i{width:40px;height:40px;background:var(--white);border-radius:50%;flex:none}
.btn{background:var(--red);color:var(--white);font-weight:700;text-transform:uppercase;display:flex;align-items:center;justify-content:center}
.call-btn{width:172px;height:53px;font-size:20px;letter-spacing:2px}
.slider-arrows{position:absolute;left:105px;top:409px;display:flex;gap:10px}
.slider-arrows svg{width:30px;height:30px}
.request{position:absolute;left:781px;top:96px;width:300px;height:345px;background:rgba(26,50,99,.88);padding:22px 27px 0}
.request h2{color:var(--white);font-size:19.5px;font-weight:700;text-align:center;text-transform:uppercase;margin-bottom:17px;margin-left:10px}
.request .field{height:34px;border:1px solid var(--red);color:#d6dbe6;font-size:10px;padding-left:16px;line-height:32px;margin-bottom:7px;background:rgba(26,50,99,.5)}
.request .btn{height:43px;font-size:14px;margin-top:4px}

/* shared headings */
.sec-title{font-size:30px;font-weight:700;color:var(--navy);text-transform:uppercase}
.sec-title em{font-style:normal;color:var(--red)}
.rule{width:52px;height:2px;background:var(--red)}
.more{font-family:"Montserrat",sans-serif;font-size:9.5px;font-weight:700;color:var(--red);letter-spacing:1px;text-transform:uppercase;display:flex;align-items:center;gap:3px}

/* about */
.about{top:713px;height:442px}
.video{position:absolute;left:104px;top:85px;width:480px;height:270px;background:linear-gradient(135deg,#6b5a4c,#a08770 45%,#3c4d6e)}
.video-bar{position:absolute;left:0;right:0;bottom:0;height:22px;background:rgba(0,0,0,.55);display:flex;align-items:center;gap:12px;padding:0 12px}
.video-bar .track{flex:1;height:3px;background:#8a8a8a}
.about-copy{position:absolute;left:642px;top:80px;width:442px}
.about-copy .rule{margin:15px 0 21px}
.about-copy p{font-size:13.5px;line-height:17.3px;color:var(--muted);margin-bottom:17px}

/* services */
.services{top:1155px;height:621px;background:var(--grey-band)}
.services .sec-title,.reviews .sec-title{text-align:center;margin-top:71px}
.services .rule,.reviews .rule{margin:21px auto 0}
.cards{position:absolute;left:98px;top:179px;display:flex;gap:28px}
.card{width:226px;height:350px;background:var(--white)}
.card h3{height:55px;background:var(--navy);color:var(--white);font-size:13.5px;font-weight:700;text-transform:uppercase;text-align:center;display:flex;align-items:center;justify-content:center;line-height:16px}
.card .photo{height:172px}
.card p{padding:18px 19px 0;font-size:10.3px;line-height:13.4px;color:#888;text-align:justify;height:72px}
.card .more{padding-left:19px;margin-top:6px}

/* reviews */
.reviews{top:1776px;height:456px}
.review{position:absolute;top:181px;width:309px}
.review .quote{position:absolute;left:22px;top:-12px;background:var(--white);padding:0 2px}
.review .box{border:2px solid #9aa3b5;height:130px;padding:23px 22px 0;position:relative}
.review .box::after{content:"";position:absolute;left:28px;bottom:-9px;width:14px;height:14px;background:var(--white);border-right:2px solid #9aa3b5;border-bottom:2px solid #9aa3b5;transform:rotate(45deg)}
.review h3{font-size:14px;font-weight:600;color:var(--navy);margin-bottom:7px}
.review p{font-size:11.8px;line-height:16px;color:var(--muted);text-align:justify}
.review .who{padding:17px 0 0 31px}
.review .who b{display:block;font-family:"Montserrat",sans-serif;color:var(--red);font-size:14px;font-weight:700;text-transform:uppercase}
.review .who span{font-size:12.5px;color:var(--navy)}
.side-arrow{position:absolute;top:234px;width:22px;height:22px;background:var(--navy)}

/* contact */
.contact{top:2232px;height:571px;background:var(--navy)}
.contact .sec-title{color:var(--white);position:absolute;top:57px}
.contact .rule{position:absolute;top:113px;width:84px;background:var(--white)}
.c-brand{position:absolute;left:104px;top:160px;display:flex;align-items:center;gap:8px}
.c-brand .brand-name{color:var(--white);font-size:19px}
.c-address{position:absolute;left:278px;top:149px;color:var(--white);font-size:14.5px;line-height:17px}
.c-address b{color:var(--red);font-family:"Montserrat",sans-serif;font-weight:600;font-size:14px;display:block}
.c-lines{position:absolute;left:505px;top:150px;width:200px;color:var(--white);font-size:14.5px;line-height:17px}
.c-lines div{display:flex;align-items:center;gap:8px;white-space:nowrap}
.c-lines i{display:inline-block;width:10px;height:10px;background:var(--red);border-radius:2px;flex:none}
.map{position:absolute;left:104px;top:221px;width:566px;height:274px;background:linear-gradient(135deg,#e9ecef,#dfe5dc 50%,#e8eaee)}
.c-form{position:absolute;left:736px;top:152px;width:345px}
.c-form .field{height:32px;background:#f2f2f2;border:1px solid #c9c9c9;color:var(--red);font-size:13.5px;padding-left:13px;line-height:30px;margin-bottom:26px}
.c-form .field.msg{height:105px;line-height:18px;padding-top:6px}
.c-form .btn{width:124px;height:38px;font-size:14px}

/* footer */
.footer{top:2803px;height:43px;background:var(--red);color:#f3d2d0;font-size:12px;display:flex;align-items:center;padding:0 99px;justify-content:space-between}
.footer .social i{width:8px;height:8px;background:#f3d2d0;margin-left:8px}
</style>
</head>
<body>

<header class="wrap site-header">
  <div class="brand"><span class="brand-mark"></span><span class="brand-name">BrisVane</span></div>
  <div class="head-info" style="left:481px">
    <b><svg width="10" height="10" viewBox="0 0 24 24"><path fill="#c8261f" d="M6.6 10.8a15 15 0 006.6 6.6l2.2-2.2a1 1 0 011-.25 11.4 11.4 0 003.6.6 1 1 0 011 1V20a1 1 0 01-1 1A17 17 0 013 4a1 1 0 011-1h3.5a1 1 0 011 1 11.4 11.4 0 00.6 3.6 1 1 0 01-.25 1z"/></svg>Call Us Now</b>
    <span>(555) 014-2290</span>
  </div>
  <div class="head-info" style="left:722px">
    <b><svg width="11" height="9" viewBox="0 0 24 18"><rect width="24" height="18" rx="2" fill="#c8261f"/><path d="M1 2l11 8 11-8" stroke="#fff" stroke-width="2" fill="none"/></svg>Contact Email</b>
    <span>hello@brisvane.example</span>
  </div>
  <div class="head-info" style="left:1003px;top:60px">
    <b>Follow Us</b>
    <div class="social"><i></i><i></i><i></i><i></i><i></i></div>
  </div>
</header>

<nav class="wrap nav">
  <a class="active" href="#" style="left:105px">Home</a>
  <a href="#" style="left:266px">About Us</a>
  <a href="#" style="left:413px">Services</a>
  <a href="#" style="left:556px">Specials</a>
  <a href="#" style="left:681px">Hearth Financing</a>
  <a href="#" style="left:878px">Content</a>
  <a href="#" style="left:1004px">Contact Us</a>
</nav>

<section class="wrap hero" role="img" aria-label="Photo of two HVAC technicians in hard hats testing rooftop air conditioning units">
  <div class="hero-copy">
    <h1>Keep your friends<br>&amp; family comfortable</h1>
    <p>We now offer a full line of sanitation services<br>to combat COVID-19!<br>Ask us about these services today</p>
  </div>
  <div class="hero-actions">
    <div class="review-btn"><i></i><span>Click here to leave us<br>a review on <b>ReviewSpot!</b></span></div>
    <div class="btn call-btn">Call Now</div>
  </div>
  <div class="slider-arrows">
    <svg viewBox="0 0 30 30"><circle cx="15" cy="15" r="14" fill="#ddd" opacity=".85"/><path d="M17 9l-6 6 6 6" stroke="#555" stroke-width="3" fill="none"/></svg>
    <svg viewBox="0 0 30 30"><circle cx="15" cy="15" r="14" fill="#ddd" opacity=".85"/><path d="M13 9l6 6-6 6" stroke="#555" stroke-width="3" fill="none"/></svg>
  </div>
  <form class="request">
    <h2>Service Request</h2>
    <div class="field">Name</div>
    <div class="field">Service</div>
    <div class="field">Email Address</div>
    <div class="field">Phone</div>
    <div class="field">Location</div>
    <div class="btn">Submit</div>
  </form>
</section>

<section class="wrap about">
  <div class="video" role="img" aria-label="Company video still of a family relaxing on a couch at home">
    <div class="video-bar">
      <svg width="12" height="12" viewBox="0 0 12 12"><path d="M2 1l9 5-9 5z" fill="#fff"/></svg>
      <div class="track"></div>
      <svg width="30" height="10" viewBox="0 0 30 10"><rect x="0" y="2" width="8" height="6" fill="#fff"/><circle cx="17" cy="5" r="4" fill="#fff"/><rect x="24" y="1" width="6" height="8" fill="none" stroke="#fff"/></svg>
    </div>
  </div>
  <div class="about-copy">
    <h2 class="sec-title">About <em>Us</em></h2>
    <div class="rule"></div>
    <p>Lorem ipsum dolor sit amet, cu per porro dolore nostro, partem integre corpora per ea, tation ornatus mel ad. Brute voluptatibus an est, per cu utroque torquatos, ei eum amet hinc. Ne vix ludus timeam definitionem. His hinc dicunt minimum cu, qui te dico laoreet. Sea ea mucius diceret insolens, eos ei nostrud appellantur, an autem vocent dolorem vel. Ne adhuc accusata eleifend has,</p>
    <p>novum doctus id mel. Id everti commune accusata melsunt explicabo. Nemo enim ipsam voluptatem quia voluptas sit aspernatur aut odit aut fugit, sed quia consequuntur magni dolores eos</p>
    <div class="more">Learn More <svg width="9" height="6" viewBox="0 0 9 6"><path d="M0 3h7M5 0l3 3-3 3" stroke="#c8261f" stroke-width="1.3" fill="none"/></svg></div>
  </div>
</section>

<section class="wrap services">
  <h2 class="sec-title">Our <em>Services</em></h2>
  <div class="rule"></div>
  <div class="cards">
    <article class="card">
      <h3>Geothermal</h3>
      <div class="photo" role="img" aria-label="Photo of geothermal steam vents across a valley" style="background:linear-gradient(180deg,#7fa6d6,#dfe6ea 55%,#a58d6a)"></div>
      <p>Varietates autem iniurasque fortunae facile veteres philosophorum praeceptis instituta vita superabat. Et quod est munus, quod opus sapientiae</p>
      <div class="more">Learn More <svg width="9" height="6" viewBox="0 0 9 6"><path d="M0 3h7M5 0l3 3-3 3" stroke="#c8261f" stroke-width="1.3" fill="none"/></svg></div>
    </article>
    <article class="card">
      <h3>Residential HVAC<br>Installation &amp; Repair</h3>
      <div class="photo" role="img" aria-label="Photo of a refrigerant manifold gauge set" style="background:linear-gradient(135deg,#3f5f8e,#c9404a 50%,#d7b33a)"></div>
      <p>Quae qui non vident, nihil umquam magnumac cognitione dignum amaverunt. Dicet pro me ipsa virtus nec dubitabit isti vestro beato M.</p>
      <div class="more">Learn More <svg width="9" height="6" viewBox="0 0 9 6"><path d="M0 3h7M5 0l3 3-3 3" stroke="#c8261f" stroke-width="1.3" fill="none"/></svg></div>
    </article>
    <article class="card">
      <h3>Commercial HVAC<br>Installation &amp; Repair</h3>
      <div class="photo" role="img" aria-label="Close-up photo of a condenser fan grille" style="background:linear-gradient(135deg,#2b2e33,#595e66 50%,#1f2226)"></div>
      <p>Cerum tamen cum de rebus grandioribus dicas, ipsae res verba rapiunt; Hoc non est positum in nostra actione. Quod ea non occurrentia nos</p>
      <div class="more">Learn More <svg width="9" height="6" viewBox="0 0 9 6"><path d="M0 3h7M5 0l3 3-3 3" stroke="#c8261f" stroke-width="1.3" fill="none"/></svg></div>
    </article>
    <article class="card">
      <h3>Maintenance Plan</h3>
      <div class="photo" role="img" aria-label="Photo of an outdoor air conditioning unit beside a brick wall" style="background:linear-gradient(90deg,#9da3aa,#c0c5cb 55%,#9a5a45)"></div>
      <p>Equidem etiam Epicurum, in physicis quidem, Democriteum puto. Responderat totidem verbis. Nemo igitur esse beatus potest. Consequens</p>
      <div class="more">Learn More <svg width="9" height="6" viewBox="0 0 9 6"><path d="M0 3h7M5 0l3 3-3 3" stroke="#c8261f" stroke-width="1.3" fill="none"/></svg></div>
    </article>
  </div>
</section>

<section class="wrap reviews">
  <h2 class="sec-title">Client's <em>Reviews</em></h2>
  <div class="rule"></div>
  <div class="side-arrow" style="left:0"><svg width="22" height="22" viewBox="0 0 22 22"><path d="M13 6l-5 5 5 5" stroke="#fff" stroke-width="1.5" fill="none"/></svg></div>
  <div class="side-arrow" style="right:0"><svg width="22" height="22" viewBox="0 0 22 22"><path d="M9 6l5 5-5 5" stroke="#fff" stroke-width="1.5" fill="none"/></svg></div>

  <div class="review" style="left:104px">
    <svg class="quote" width="26" height="20" viewBox="0 0 26 20"><path d="M0 20V10Q0 2 9 0v4Q5 5 5 9h5v11zM14 20V10q0-8 9-10v4q-4 1-4 5h5v11z" fill="#1a3263"/></svg>
    <div class="box"><h3>Highly Professional Team</h3><p>Lorem ipsum dolor sit amet, consectetur adipiscing elit. Quid autem habent admirationis, cum prope accesseris? An hoc usque quaque, aliter in vita?</p></div>
    <div class="who"><b>Marcus Ellery</b><span>Manager</span></div>
  </div>
  <div class="review" style="left:441px">
    <svg class="quote" width="26" height="20" viewBox="0 0 26 20"><path d="M0 20V10Q0 2 9 0v4Q5 5 5 9h5v11zM14 20V10q0-8 9-10v4q-4 1-4 5h5v11z" fill="#1a3263"/></svg>
    <div class="box"><h3>Highly Professional Team</h3><p>Lorem ipsum dolor sit amet, consectetur adipiscing elit. Quid autem habent admirationis, cum prope accesseris? An hoc usque quaque, aliter in vita?</p></div>
    <div class="who"><b>Dana Whitlock</b><span>Top Manager</span></div>
  </div>
  <div class="review" style="left:775px">
    <svg class="quote" width="26" height="20" viewBox="0 0 26 20"><path d="M0 20V10Q0 2 9 0v4Q5 5 5 9h5v11zM14 20V10q0-8 9-10v4q-4 1-4 5h5v11z" fill="#1a3263"/></svg>
    <div class="box"><h3>Highly Professional Team</h3><p>Lorem ipsum dolor sit amet, consectetur adipiscing elit. Quid autem habent admirationis, cum prope accesseris? An hoc usque quaque, aliter in vita?</p></div>
    <div class="who"><b>Owen Pratt</b><span>Consultant</span></div>
  </div>
</section>

<section class="wrap contact">
  <h2 class="sec-title" style="left:102px">Contact <em>Us</em></h2>
  <div class="rule" style="left:104px"></div>
  <h2 class="sec-title" style="left:736px">Submit <em>Info</em></h2>
  <div class="rule" style="left:736px"></div>

  <div class="c-brand"><span class="brand-mark" style="width:18px;height:18px"></span><span class="brand-name">BrisVane</span></div>
  <div class="c-address"><b>BrisVane Comfort Works, LLC</b>418 Ridgeline Ave,<br>Brisvane, OK 70012</div>
  <div class="c-lines">
    <div><i></i>(555) 014-2290</div>
    <div><i></i>hello@brisvane.example</div>
    <div><i></i>www.brisvaneair.example</div>
  </div>
  <div class="map" role="img" aria-label="Street map showing the company location"></div>

  <form class="c-form">
    <div class="field">Name*</div>
    <div class="field">Email*</div>
    <div class="field">Subject</div>
    <div class="field msg">Message</div>
    <div class="btn">Send</div>
  </form>
</section>

<footer class="wrap footer">
  <span>Copyright 2020, service Summit Web Partners, All Right Reserved</span>
  <div class="social"><i></i><i></i><i></i><i></i><i></i></div>
</footer>

</body>
</html>
```